Signage for Brightwell Academy - Exterior

Size 32 ft x 5 ft 11 inches. It will be installed at a height of 25 feet. Should contain the Logo, Address, some courses to give an idea about what we do. The signage is installed on the 2nd floor, so the minimum size of letters would be as in the old signage design attached. The font size of the bottom line of our existing signage is as small as we should go. Basically it should be such that the first glance gives us an idea that it is a Brightwell Academy. You are allowed to change the logo colors, but the font and design will remain the same.
Updates

Reason: some extra time might be needed to improve the designs and get new inputs. need some out of the box designing.

Target Market(s)

High School and College going teens who wish to learn software skills for graphics and animation

Industry/Entity Type

Education

Font styles to use
Other font styles liked:
• Utopia

Colors

Designer to choose colors to be used in the design.

Requirements
Must have
• Logo, Address, Phone Number, website address, what we do.
• 1. Please refer to the image of our old signage uploaded. The font size of the courses mentioned at the bottom of the signage "ANIMATION, GAMING.." is the smallest size which is legible from the ground level.
• 2. We would like at least the web address in legible font size and if possible the phone number too. The physical address could be a little smaller as in the old signage, as that is not a calling factor and in case someone is interested, they can walk closer and read the address.
• 3. The calling factors would be a few courses and some graphics depicting what we do in the first look.
• 4.You are allowed to change the logo colors, but the font and design will remain the same. Prefer usage of Ubuntu font for text.
• 5. Prefer minimalist look and not cluttered. I feel mentioning more courses is making the signage cluttered. we can limit it to 3 courses.
Nice to have
• Graphics to suggest what we do. It should be eye catching. The graphic should be such that speaks of what we do. It should be suggestive.
Should not have
• It should not be too busy

```html
<!DOCTYPE html>
<html lang="en">
<head>
<meta charset="utf-8">
<title>Brightwell Academy – Exterior Signage</title>
<link rel="stylesheet" href="https://fonts.googleapis.com/css2?family=Ubuntu:wght@400;500;700&display=swap">
<style>
  :root {
    --page-bg: #f4f4f4;
    --sign-navy: #0a1638;
    --sign-navy-deep: #040919;
    --accent-cyan: #2ec6e8;
    --text-white: #ffffff;
    --text-soft: #e6ecf5;
  }
  * { box-sizing: border-box; margin: 0; padding: 0; }
  html, body {
    width: 1200px;
    height: 848px;
    overflow: hidden;
    background: var(--page-bg);
    font-family: "Ubuntu", sans-serif;
  }
  .canvas {
    position: relative;
    width: 1200px;
    height: 848px;
  }
  .signboard {
    position: absolute;
    left: 41px;
    top: 318px;
    width: 1122px;
    height: 212px;
    background: linear-gradient(90deg, var(--sign-navy) 0%, #07112c 55%, var(--sign-navy-deep) 100%);
    box-shadow: 3px 4px 6px rgba(0, 0, 0, 0.35);
    color: var(--text-white);
  }
  .brand {
    position: absolute;
    left: 32px;
    top: 22px;
    width: 340px;
    text-align: right;
  }
  .brand-name {
    display: block;
    font-weight: 500;
    font-size: 60px;
    line-height: 56px;
    letter-spacing: 2px;
    color: var(--accent-cyan);
    text-align: left;
  }
  .brand-tagline {
    display: block;
    margin-top: 14px;
    font-weight: 500;
    font-size: 22px;
    letter-spacing: 1px;
    color: var(--text-white);
  }
  .divider {
    position: absolute;
    left: 408px;
    top: 14px;
    width: 2px;
    height: 174px;
    background: var(--text-white);
  }
  .course-list {
    position: absolute;
    left: 439px;
    top: 34px;
    list-style: none;
    font-weight: 500;
    font-size: 22px;
    line-height: 28px;
    letter-spacing: 2.6px;
    color: var(--text-white);
  }
  .contact {
    position: absolute;
    left: 855px;
    top: 78px;
    color: var(--text-white);
  }
  .contact-city {
    font-size: 13px;
    letter-spacing: 1.5px;
    line-height: 14px;
  }
  .contact-web {
    font-weight: 700;
    font-size: 20px;
    letter-spacing: 1.6px;
    line-height: 22px;
  }
  .contact-address {
    margin-top: 14px;
    font-size: 12px;
    font-weight: 500;
    letter-spacing: 1px;
    line-height: 15px;
    color: var(--text-soft);
  }
  .contact-phone {
    position: relative;
    font-size: 12px;
    font-weight: 500;
    letter-spacing: 1.4px;
    line-height: 15px;
  }
  .phone-icon {
    position: absolute;
    left: -27px;
    top: -9px;
    width: 20px;
    height: 20px;
  }
</style>
</head>
<body>
<main class="canvas">
  <section class="signboard" aria-label="Brightwell Academy exterior sign">
    <div class="brand">
      <span class="brand-name">BRIGHT<br>WELL</span>
      <span class="brand-tagline">digital academy</span>
    </div>

    <div class="divider" aria-hidden="true"></div>

    <ul class="course-list">
      <li>animation</li>
      <li>gaming</li>
      <li>vfx</li>
      <li>film making</li>
      <li>web &amp; graphic design</li>
    </ul>

    <address class="contact" style="font-style: normal;">
      <p class="contact-city">LAKEVIEW</p>
      <p class="contact-web">www.brightwell.in</p>
      <p class="contact-address">Plot 12-14, First Floor,<br>Block 7 B</p>
      <p class="contact-phone">
        <svg class="phone-icon" viewBox="0 0 24 24" aria-hidden="true">
          <circle cx="12" cy="12" r="11" fill="var(--text-white)"/>
          <path d="M8.2 6.5c.5-.4 1.1-.3 1.4.2l1.2 2c.3.5.2 1-.2 1.3l-.8.6c.6 1.4 1.7 2.6 3.1 3.3l.6-.8c.3-.4.9-.5 1.3-.2l2 1.2c.5.3.6.9.2 1.4l-.8 1c-.6.6-1.5.8-2.3.5-3.2-1.3-5.6-3.8-6.9-7-.3-.8-.1-1.7.5-2.3z" fill="var(--sign-navy)"/>
        </svg>
        0100 555 0199
      </p>
    </address>
  </section>
</main>
</body>
</html>
```